Home Page Redesign for Pet Website

Looking to redesign the home page of our WORDPRESS website which will be renamed The Critter Cover Handbook 2015.

Looking for clean design which communicates clarity.
Updates

This is for a Wordpress site.

Please note that the design MUST include the content which is shown in the table in the brief!

Hi Thanks for the designs so far. We have just updated the brief to provide more information and clarify a few issues. We have also now included a couple of layout suggestions. They are just suggestions but it should give you a better idea of what we are looking for. And we have just increased the budget for 1st place by £120. Please feel free to message me if you have any questions. Many thanks. Maud

Please note that the new brief is in a file dated 25 Jan!

Reason: We have extended the deadline so we can continue working with the designers who have submitted designs we like. If you have any new designs please submit them by the original deadline of 7.37pm this evening (GMT). We are planning to make our final decision by Friday this week.

Target Market(s)

UK pet owners. All ages but largest age group is 35-50.

Industry/Entity Type

Insurance

Requirements
Must have
• Three clear content groups - LEARN, RESEARCH, CAMPAIGN (see brief for more details).
Stock photos with dogs and cats
Use current colour scheme
Must work with existing inner pages.
Existing font.. but 1pt larger
See brief for more details
Should not have
• Logo
Content from Existing Page (except for footer content... and menu headings).

```html
<!DOCTYPE html>
<html lang="en">
<head>
<meta charset="utf-8">
<title>The Critter Cover Handbook 2015</title>
<link href="https://fonts.googleapis.com/css2?family=Roboto+Slab:wght@400;700&family=Open+Sans:ital,wght@0,400;0,600;1,600&display=swap" rel="stylesheet">
<style>
:root{
  --blue:#8ab8ee;
  --blue-text:#6fa8e8;
  --blue-dark:#2a6fb8;
  --ink:#1a1a1a;
  --body:#333;
  --muted:#888;
  --line:#d9d9d9;
  --bullet:#e07b39;
  --black:#000;
  --red:#c0292f;
  --tick:#b3242a;
  --paper:#fff;
}
*{margin:0;padding:0;box-sizing:border-box}
html,body{width:695px;height:1200px;overflow:hidden;background:var(--paper)}
body{font-family:Arial,Helvetica,sans-serif;color:var(--body)}
.canvas{position:relative;width:695px;height:1200px;overflow:hidden}
.abs{position:absolute}
.slab{font-family:'Roboto Slab',Georgia,serif}
.sans{font-family:'Open Sans',Arial,sans-serif}

.top-rule{left:0;top:0;width:695px;height:2px;background:var(--blue)}
.site-title{left:86px;top:10px;font:700 16px 'Roboto Slab',Georgia,serif;color:var(--ink);letter-spacing:.2px}
.site-title span{color:var(--blue-text)}
.tagline{left:86px;top:36px;font:400 9px 'Roboto Slab',Georgia,serif;color:var(--ink)}
.phone{left:514px;top:9px;font:400 12px Arial,sans-serif;color:#222;display:flex;align-items:center;gap:4px}
.search{left:462px;top:32px;width:116px;height:14px;border:1px solid var(--line);font-size:6px;color:#aaa;padding:3px 4px}
.go{left:585px;top:32px;width:23px;height:14px;background:var(--blue);font:700 8px Arial,sans-serif;color:#111;text-align:center;line-height:14px}

.nav{left:0;top:54px;width:695px;height:28px;background:var(--blue)}
.nav ul{list-style:none;display:flex;position:absolute;left:84px;top:0;height:28px;align-items:center}
.nav li{font:400 8px Arial,sans-serif;color:#fff;padding:0 9px;line-height:28px;border-right:1px solid rgba(255,255,255,.35)}
.nav li:last-child{border-right:0}
.nav li.current{color:#111}

.hero{left:0;top:82px;width:695px;height:190px;background:var(--black)}
.hero-photo{left:85px;top:82px;width:523px;height:190px;background:linear-gradient(180deg,#fafafa 0%,#f1ede6 45%,#cdb9a0 75%,#7d6a5a 100%)}
.hero-caption{left:85px;top:249px;width:523px;height:23px;background:rgba(60,60,60,.75);color:#fff;font:400 14px 'Roboto Slab',Georgia,serif;text-align:center;line-height:23px}
.arrow{top:164px;width:19px;height:19px;display:flex;align-items:center;justify-content:center}
.arrow.prev{left:66px;background:#777}
.arrow.next{left:608px;background:var(--blue)}

.card{border:1px solid var(--line);background:#fff}
.card h2{font:400 10.5px 'Roboto Slab',Georgia,serif;color:var(--ink);margin:6px 6px 0;padding-bottom:4px;border-bottom:1px solid #e6e6e6;display:inline-block;padding-right:20px}
.card h2 span{color:var(--blue-text)}
.card p{font-size:7px;line-height:10.3px;color:var(--body);margin:7px 6px 0}
.list{list-style:none;font:400 7.4px 'Open Sans',Arial,sans-serif;color:#333}
.list li{position:relative;padding-left:12px;margin-bottom:5px;line-height:9px}
.list li::before{content:"";position:absolute;left:0;top:1px;width:5px;height:5px;border:1px solid var(--bullet);border-radius:50%;background:radial-gradient(circle,var(--bullet) 35%,transparent 40%)}
.more{font:400 7.5px 'Roboto Slab',Georgia,serif;color:var(--blue-text);border-bottom:1px solid #ccc;padding-bottom:1px}

.ad{border:1px solid #cfcfcf;background:linear-gradient(180deg,#f6f3ee,#ece6dc)}
.ad-name{font:400 22px 'Roboto Slab',Georgia,serif;color:#8d8b85}
.ad-sub{font:400 8.5px 'Roboto Slab',Georgia,serif;color:#777}
.ad-photo{background:radial-gradient(circle at 40% 45%,#c47a3a,#8b4a1c 55%,#5b8fb5 80%,#ece6dc 95%)}
.ad-points{list-style:none;font:700 8px Arial,sans-serif;color:var(--tick)}
.ad-points li{display:flex;gap:4px;margin-bottom:3px;line-height:8.5px}
.ad-btn{background:var(--red);color:#fff;font:700 7.5px Arial,sans-serif;text-align:center;border-radius:2px}
.ad-offer{font:700 8px Arial,sans-serif;color:#111}
.ad-fine{font-size:5.2px;color:#777}

.side-text{font-size:6.6px;line-height:10.4px;color:#333}

.footer{left:0;top:954px;width:695px;height:222px;background:var(--blue)}
.widget{background:#fff;border-radius:3px;overflow:hidden}
.widget-head{height:21px;font:600 9.5px 'Open Sans',Arial,sans-serif;color:var(--blue-dark);display:flex;align-items:center;gap:5px;padding-left:6px}
.mark{width:9px;height:9px;background:var(--blue-dark);display:inline-block}
.avatar{background:linear-gradient(160deg,#b48b73,#5a4a44)}
.tweet{font-size:6px;line-height:8px;color:#333}
.follow-btn{background:#fff;border:1px solid #ccc;border-radius:2px;font:700 9px Arial,sans-serif;color:#222;display:flex;align-items:center;gap:5px;padding:0 6px}
.foot-title{font:700 14px 'Roboto Slab',Georgia,serif;color:var(--ink);text-align:center;line-height:18px}
.copyright{left:0;top:1176px;width:695px;height:24px;background:var(--black);color:#ddd;font-size:6px;text-align:center;line-height:24px}
</style>
</head>
<body>
<div class="canvas">

  <div class="abs top-rule"></div>
  <div class="abs site-title">THE CRITTER COVER <span>HANDBOOK 2015</span></div>
  <div class="abs tagline">Independent Unbiased Information For Fellow Pet Owners</div>
  <div class="abs phone">
    <svg width="11" height="11" viewBox="0 0 12 12"><circle cx="6" cy="6" r="5.3" fill="none" stroke="#222" stroke-width="1"/><path d="M4 3.3l1 1.2-.6.8c.4.9 1.2 1.6 2.1 2.1l.8-.6 1.2 1-.6 1c-2.3-.3-4.2-2.2-4.6-4.5z" fill="#222"/></svg>
    020-555-0142
  </div>
  <div class="abs search">search here......</div>
  <div class="abs go">GO</div>

  <nav class="abs nav">
    <ul>
      <li class="current">HOME</li>
      <li>LEARN About Pet Insurance</li>
      <li>RESEARCH Pet Insurance Policies</li>
      <li>CAMPAIGN For Fairer Pet Insurance</li>
      <li>CONTACT US</li>
    </ul>
  </nav>

  <div class="abs hero"></div>
  <div class="abs hero-photo" role="img" aria-label="Photo of a row of dogs and cats sitting together on a white background"></div>
  <div class="abs hero-caption">Independent Unbiased Information For Fellow Pet Owners</div>
  <div class="abs arrow prev"><svg width="7" height="9" viewBox="0 0 7 9"><path d="M5 1L2 4.5 5 8" fill="none" stroke="#fff" stroke-width="1.4"/></svg></div>
  <div class="abs arrow next"><svg width="7" height="9" viewBox="0 0 7 9"><path d="M2 1l3 3.5L2 8" fill="none" stroke="#fff" stroke-width="1.4"/></svg></div>

  <!-- LEARN -->
  <section class="abs card" style="left:79px;top:294px;width:338px;height:154px">
    <h2>LEARN <span>About Pet Insurance</span></h2>
    <p>Lorem ipsum dolor sit amet, consectetuer adipiscing elit, sed diam nonummy nibh isaincidunt ut laoreet dolore magna aliquam erat volutpat. Ut wisi enim ad minim veniam, quisstruexerci tation ullamcorper suscipit lobortis nisl ut aliquip accumsan et iusto odio enim..</p>
    <ul class="abs list" style="left:6px;top:65px;width:165px">
      <li>Vet Fees Cover Types</li>
      <li>What to Consider before Buying</li>
      <li>Ten Popular Pet Insurance Providers</li>
      <li>Confused by Pet Insurance: &nbsp;Start Here!</li>
      <li>Third Party Liability Insurance</li>
    </ul>
    <ul class="abs list" style="left:173px;top:65px;width:160px">
      <li>Six Vet Fees Pet Insurance Companies Won't Pay!</li>
      <li>Why Cheap Pet Insurance is Risky</li>
      <li>Why Your Pets Vet History is Important</li>
    </ul>
    <span class="abs more" style="left:287px;top:137px">Read More</span>
  </section>

  <!-- Ad 1 -->
  <aside class="abs ad" style="left:432px;top:294px;width:176px;height:154px">
    <div class="abs ad-name" style="left:14px;top:-2px">pawsure</div>
    <div class="abs ad-sub" style="left:16px;top:29px">Medical insurance for your pet.</div>
    <div class="abs ad-photo" role="img" aria-label="Puppy playing with a blue ball" style="left:2px;top:42px;width:80px;height:92px;border-radius:40%"></div>
    <ul class="abs ad-points" style="left:84px;top:50px">
      <li><svg width="12" height="10" viewBox="0 0 12 10"><path d="M1 5l3.5 3.5L11 1" fill="none" stroke="#b3242a" stroke-width="2.2"/></svg><span>One<br>Simple Plan</span></li>
      <li><svg width="12" height="10" viewBox="0 0 12 10"><path d="M1 5l3.5 3.5L11 1" fill="none" stroke="#b3242a" stroke-width="2.2"/></svg><span>90% Coverage</span></li>
      <li><svg width="12" height="10" viewBox="0 0 12 10"><path d="M1 5l3.5 3.5L11 1" fill="none" stroke="#b3242a" stroke-width="2.2"/></svg><span>No<br>Payout Limits</span></li>
    </ul>
    <div class="abs ad-btn" style="left:88px;top:111px;width:67px;height:15px;line-height:15px">FREE QUOTE ▸</div>
    <div class="abs ad-offer" style="left:77px;top:132px">Get $10 off enrollment</div>
    <div class="abs ad-fine" style="left:16px;top:145px">Exclusions may apply. See policy for full details.</div>
  </aside>

  <!-- RESEARCH -->
  <section class="abs card" style="left:79px;top:464px;width:338px;height:213px">
    <h2>Research <span>UK Pet Insurance Policies</span></h2>
    <p style="font-size:7.5px">Analysis, Customer Reviews and Full Details of All UK Policies</p>
    <ul class="abs list" style="left:6px;top:45px;width:160px">
      <li>Paw Partners</li><li>Hartwell</li><li>Straight Path</li><li>B&amp;K</li><li>Happy Tails</li><li>Covermate</li><li>Harold Pike</li><li>NM= Northgate Mutual</li>
    </ul>
    <ul class="abs list" style="left:173px;top:44px;width:160px">
      <li>Hound Society</li><li>R&amp;T</li><li>Plus One Pet Insurance</li><li>Furplan</li><li>Brambley's Finance</li><li>Corvo</li><li>Beacon Money</li><li>Other Providers</li>
    </ul>
    <div class="abs sans" style="left:5px;top:165px;font-style:italic;font-weight:600;font-size:9px;line-height:14.5px;color:#222">Search Our Database For Policies Matching Your Criteria<br>Compare Claims Experiences &nbsp;For Pet Insurance Providers</div>
    <span class="abs more" style="left:287px;top:195px">Read More</span>
  </section>

  <!-- Biography -->
  <aside class="abs card" style="left:430px;top:464px;width:178px;height:174px;border-radius:3px">
    <h2 style="width:164px">Biography</h2>
    <div class="abs" role="img" aria-label="Portrait photo of a young dog" style="left:10px;top:26px;width:50px;height:50px;border-radius:50%;background:radial-gradient(circle,#8a6b4a,#3b3027 60%,#cfd9e2 62%)"></div>
    <div class="abs side-text" style="left:88px;top:30px;line-height:9px">Lorem Ispum<br>Autem</div>
    <div class="abs side-text" style="left:87px;top:63px">Lorem Isum, Autem</div>
    <div class="abs side-text" style="left:7px;top:84px;width:166px">Ut wisi enim ad minim veniam, quis nostrud exerc ree orper suscipit lobortis nisl ut aliquip ex ea commodor consequat. Duis autem vel eum. Lorem ipsum is ther dummpy text of the insustry.</div>
    <div class="abs side-text" style="left:7px;top:128px;width:166px">Ut wisi enim ad minim veniam, quis nostrud exerc ullamcade orper suscipit lobortis.</div>
    <span class="abs more" style="left:123px;top:155px">Read More</span>
  </aside>

  <!-- Disclaimer -->
  <aside class="abs card" style="left:431px;top:656px;width:177px;height:141px;border-radius:3px">
    <h2 style="width:164px">Disclaimer</h2>
    <div class="abs side-text" style="left:5px;top:26px;width:170px">Please note that pet insurance terms often change. Whilst we will do our best to keep this website up to date you must check with the appropriate insurer before making any decisions. If you find any mistakes on this website please do let us know so we can correct it for the benefit of future visitors. Many thanks! -</div>
    <div class="abs side-text" style="left:5px;top:104px;width:170px;color:#111"><b>See more at:</b><br>www.critter-cover-surveys.co.uk/insurer-list/#ref.k2Pq7Lm</div>
  </aside>

  <!-- Ad 2 -->
  <aside class="abs ad" style="left:432px;top:814px;width:176px;height:116px">
    <div class="abs ad-name" style="left:14px;top:-4px">pawsure</div>
    <div class="abs ad-sub" style="left:16px;top:22px;font-size:7.5px">Medical insurance for your pet.</div>
    <div class="abs ad-photo" role="img" aria-label="Puppy playing with a blue ball" style="left:2px;top:33px;width:74px;height:72px;border-radius:40%"></div>
    <ul class="abs ad-points" style="left:84px;top:38px;font-size:6.5px">
      <li><svg width="10" height="8" viewBox="0 0 12 10"><path d="M1 5l3.5 3.5L11 1" fill="none" stroke="#b3242a" stroke-width="2.2"/></svg><span>One<br>Simple Plan</span></li>
      <li><svg width="10" height="8" viewBox="0 0 12 10"><path d="M1 5l3.5 3.5L11 1" fill="none" stroke="#b3242a" stroke-width="2.2"/></svg><span>90% Coverage</span></li>
      <li><svg width="10" height="8" viewBox="0 0 12 10"><path d="M1 5l3.5 3.5L11 1" fill="none" stroke="#b3242a" stroke-width="2.2"/></svg><span>No<br>Payout Limits</span></li>
    </ul>
    <div class="abs ad-btn" style="left:88px;top:85px;width:66px;height:12px;line-height:12px;font-size:6.5px">FREE QUOTE ▸</div>
    <div class="abs ad-offer" style="left:78px;top:100px;font-size:6.8px">Get $10 off enrollment</div>
    <div class="abs ad-fine" style="left:18px;top:110px;font-size:4.8px">Exclusions may apply. See policy for full details.</div>
  </aside>

  <!-- CAMPAIGN -->
  <section class="abs card" style="left:79px;top:693px;width:338px;height:150px">
    <h2>Campaign <span>For Fairer Pet Insurance</span></h2>
    <div class="abs sans" style="left:6px;top:32px;width:320px;font-size:7.4px;line-height:10.3px;color:#333">
      <p style="margin:0 0 5px">Loremre ipsum dolor sit amet, consectetuer adipiscing elit, sed diam nonummy nibh rerunt ut laoreet dolore magna aliquam erat volutpat. Ut wisi enim ad minim veniam, quis loremis nostruexerci tation ullamcorper suscipit lobortis nisl.</p>
      <p style="margin:0 0 10px">Loremre ipsum dolor sit amet, consectetuer adipiscing elit, sed diam nonummy nibh rerunt ut laoreet dolore magna aliquam erat volutpat.</p>
      <p style="margin:0">Loremre ipsum dolor sit amet, consectetuer adipiscing elit, sed diam nonummy nibh rerunt ut laoreet dolore magna aliquam erat volutpat. Ut wisi enim ad minim veniam, quis loremis nostruexerci tation ullamcorper suscipit.</p>
    </div>
    <span class="abs more" style="left:287px;top:133px">Read More</span>
  </section>

  <!-- POPULAR -->
  <section class="abs card" style="left:79px;top:860px;width:338px;height:70px">
    <h2>Popular <span>Resources</span></h2>
    <div class="abs sans" style="left:6px;top:26px;width:320px;font-size:7.4px;line-height:10.3px;color:#333">Loremre ipsum dolor sit amet, consectetuer adipiscing elit, sed diam nonummy nibh rerunt ut laoreet dolore magna aliquam erat volutpat.</div>
    <ul class="abs list" style="left:6px;top:52px;display:flex;gap:28px;font-size:7.8px"><li>Lorem Ispum</li><li>Lorem Ispum</li></ul>
    <span class="abs more" style="left:285px;top:53px">Read More</span>
  </section>

  <!-- FOOTER -->
  <footer class="abs footer">
    <div class="abs widget" style="left:91px;top:16px;width:153px;height:190px">
      <div class="widget-head" style="background:#e4ebf4"><span class="mark"></span>Join us on Pawbook</div>
      <div class="abs avatar" role="img" aria-label="Profile photo" style="left:6px;top:26px;width:26px;height:26px"></div>
      <div class="abs" style="left:36px;top:28px;font:700 7px Arial,sans-serif;color:var(--blue-dark)">Critter Cover Surveys UK</div>
      <div class="abs" style="left:36px;top:40px;font:6px Arial,sans-serif;color:#333"><span style="background:var(--blue-dark);color:#fff;padding:1px 3px;font-weight:700">Like</span> 1,176</div>
      <div class="abs" style="left:6px;top:60px;width:135px;height:128px;border:1px solid #ddd;border-bottom:0">
        <div class="abs avatar" role="img" aria-label="Profile photo" style="left:6px;top:6px;width:20px;height:20px"></div>
        <div class="abs" style="left:32px;top:6px;font:700 6.8px Arial,sans-serif;color:var(--blue-dark);line-height:9px">Critter Cover Surveys<br>UK</div>
        <div class="abs" style="left:32px;top:27px;font-size:5px;color:#999">January 18 at 11:43pm</div>
        <div class="abs tweet" style="left:6px;top:42px;width:125px;font-size:6.3px;line-height:9px">Pet Insurance Premium Increases</div>
        <div class="abs tweet" style="left:6px;top:56px;width:125px;font-size:6.2px;line-height:8.5px">Interesting article from Pet Matters suggesting that that pet insurance premiums can double as your pet ages...</div>
        <div class="abs tweet" style="left:6px;top:98px;width:125px;font-size:6.2px;line-height:8.5px">Have to confess that this sounds on the low side to me! Would be really</div>
      </div>
      <div class="abs" style="left:146px;top:60px;width:7px;height:130px;background:#eee"><div style="margin:8px 1px;height:28px;background:#bbb"></div></div>
    </div>

    <div class="abs widget" style="left:266px;top:16px;width:152px;height:190px">
      <div class="widget-head" style="background:#7ccfe0;color:#1d5c8f"><span class="mark" style="background:#1d5c8f;border-radius:50%"></span>Latest from Chirper</div>
      <div class="abs" style="left:6px;top:27px;font:700 7px Arial,sans-serif;color:#222">Posts</div>
      <div class="abs" style="left:114px;top:26px;width:34px;height:10px;border:1px solid #ccc;border-radius:2px;font:700 5.5px Arial,sans-serif;text-align:center;line-height:9px">Follow</div>
      <div class="abs tweet" style="left:6px;top:40px;width:135px;color:#999">have already completed our survey?<br><span style="color:var(--blue-dark)">go.to/cc15sv</span></div>
      <div class="abs avatar" role="img" aria-label="Profile photo" style="left:6px;top:72px;width:14px;height:14px"></div>
      <div class="abs tweet" style="left:24px;top:72px;font-weight:700;font-size:6px">Critter Cover Surveys</div>
      <div class="abs tweet" style="left:120px;top:72px;font-size:5.5px;color:#888">26 Sep</div>
      <div class="abs tweet" style="left:24px;top:80px;font-size:5.5px;color:#888">@CritterCoverUK</div>
      <div class="abs tweet" style="left:6px;top:92px;width:135px">Know someone who has made a pet insurance claim in the last year? Please ask them to tell us about it. Please share!<br><span style="color:var(--blue-dark)">go.to/cc15rt</span></div>
      <div class="abs tweet" style="left:6px;top:130px;color:#888;font-size:5.5px">Expand</div>
      <div class="abs avatar" role="img" aria-label="Profile photo" style="left:6px;top:145px;width:14px;height:14px"></div>
      <div class="abs tweet" style="left:24px;top:145px;font-weight:700;font-size:6px">Critter Cover Surveys</div>
      <div class="abs tweet" style="left:120px;top:145px;font-size:5.5px;color:#888">26 Sep</div>
      <div class="abs" style="left:4px;top:167px;width:144px;height:15px;border:1px solid #ccc;font-size:6px;color:#888;padding:3px 4px">Post to @CritterCoverUK</div>
      <div class="abs" style="left:145px;top:40px;width:6px;height:118px;background:#eee"><div style="margin:10px 1px;height:10px;background:#bbb"></div></div>
    </div>

    <div class="abs slab" style="left:442px;top:20px;font-size:10px;color:#111">Follow Us</div>
    <div class="abs follow-btn" style="left:443px;top:39px;width:153px;height:18px"><span class="mark" style="background:#4a9ad4"></span>Follow @CritterCoverUK</div>
    <div class="abs follow-btn" style="left:443px;top:62px;width:47px;height:18px;background:#3d5f99;color:#fff;border-color:#3d5f99"><span class="mark" style="background:#fff"></span>Like</div>
    <div class="abs follow-btn" style="left:443px;top:85px;width:74px;height:18px;font-size:8px"><span class="mark" style="background:#d34836"></span>Follow</div>
    <div class="abs foot-title" style="left:432px;top:169px;width:182px">THE CRITTER COVER<br>HANDBOOK 2015</div>
  </footer>

  <div class="abs copyright">Copyright © 2015. &nbsp;TheCritterCoverHandbook2015. &nbsp;All Rights Reserved.</div>
</div>
</body>
</html>
```